Kelvo Tech Oz Business card revamp

We are looking to revamp our business card design. We are hoping to change our colours to dark navey blue, gray, white and black but are open to keeping the same if a good design is submited. We are after somthing a bit differnt not just boring business card. I have attached a copy of our current card. We Want to keep the same logo design which i have attached a few to hopfully help you in this process. We are after a design that can be personalized to separate 4 people

Colors
0455a3
ffffff
000000
cbcbcb

Requirements
Must have
• Kelvo Tech Logo, address 3/41 Mallory Court, Wexhill 4218, phone number, Name and position

```html
<!DOCTYPE html>
<html lang="en">
<head>
<meta charset="utf-8">
<title>Kelvo Tech Business Card</title>
<link href="https://fonts.googleapis.com/css2?family=Lato:wght@400;700;900&display=swap" rel="stylesheet">
<style>
  :root {
    --navy: #123a7f;
    --navy-deep: #0b2557;
    --orange: #d8401a;
    --ink: #1c1c1c;
    --card: #f3f4f6;
    --card-edge: #e3e6eb;
    --page: #d9d9d9;
  }
  * { margin: 0; padding: 0; box-sizing: border-box; }
  html, body { width: 1200px; height: 970px; overflow: hidden; background: var(--page); }
  .business-card {
    position: absolute; left: 80px; top: 188px;
    width: 1040px; height: 594px;
    background: linear-gradient(160deg, var(--card) 0%, var(--card-edge) 100%);
    font-family: "Lato", sans-serif; color: var(--ink);
    overflow: hidden;
    box-shadow: 0 18px 40px rgba(0,0,0,0.18);
  }
  .band-top {
    position: absolute; left: 400px; top: 0; width: 640px; height: 96px;
    background: linear-gradient(90deg, rgba(18,58,127,0.35) 0%, var(--navy) 40%, var(--navy) 100%);
  }
  .band-bottom {
    position: absolute; left: 0; bottom: 0; width: 1040px; height: 112px;
    background: linear-gradient(90deg, var(--navy-deep) 0%, var(--navy) 60%, rgba(18,58,127,0.2) 100%);
  }
  .rule { position: absolute; height: 8px; background: var(--orange); }
  .rule-top { left: 380px; top: 104px; width: 660px; }
  .rule-bottom { left: 0; bottom: 124px; width: 880px; }
  .brand { position: absolute; left: 70px; top: 222px; display: flex; align-items: center; gap: 18px; }
  .brand-dot { width: 80px; height: 80px; border-radius: 50%; background: var(--navy); flex: none; }
  .brand-name { font-weight: 900; font-size: 58px; line-height: 1; color: var(--navy); letter-spacing: -1px; }
  .brand-tagline { margin-top: 8px; font-weight: 900; font-size: 23px; color: var(--navy); }
  .contact { position: absolute; left: 624px; top: 158px; }
  .person-name { font-size: 42px; font-weight: 700; line-height: 1; color: var(--navy); }
  .person-name .surname { color: var(--orange); }
  .person-role { font-size: 27px; margin-top: 4px; }
  .contact-lines { margin-top: 44px; list-style: none; }
  .contact-lines li { display: flex; align-items: center; gap: 14px; font-size: 28px; height: 38px; }
  .contact-icon { width: 30px; height: 30px; border-radius: 4px; background: var(--orange); display: flex; align-items: center; justify-content: center; }
  .address { margin-top: 22px; font-size: 28px; line-height: 35px; }
</style>
</head>
<body>
  <div class="business-card">
    <div class="band-top" role="img" aria-label="Navy decorative band"></div>
    <div class="rule rule-top"></div>
    <div class="rule rule-bottom"></div>
    <div class="band-bottom" role="img" aria-label="Navy decorative band"></div>

    <div class="brand">
      <span class="brand-dot"></span>
      <div>
        <div class="brand-name">Kelvo Tech</div>
        <div class="brand-tagline">Passive Fire Protection</div>
      </div>
    </div>

    <div class="contact">
      <div class="person-name">Dara <span class="surname">Wilkes</span></div>
      <div class="person-role">Manager</div>
      <ul class="contact-lines">
        <li>
          <span class="contact-icon">
            <svg width="20" height="20" viewBox="0 0 20 20"><path d="M3 7 C3 4 17 4 17 7 L15 9 L13 7 L7 7 L5 9 Z M6 10 L14 10 L16 16 L4 16 Z" fill="#fff"/></svg>
          </span>
          07 4410 2286
        </li>
        <li>
          <span class="contact-icon">
            <svg width="20" height="20" viewBox="0 0 20 20" fill="none" stroke="#fff" stroke-width="1.6"><circle cx="10" cy="10" r="7"/><ellipse cx="10" cy="10" rx="3" ry="7"/><line x1="3" y1="10" x2="17" y2="10"/></svg>
          </span>
          www.kelvotech.com.au
        </li>
      </ul>
      <div class="address">3/41 Mallory Court<br>Wexhill, Qld 4218</div>
    </div>
  </div>
</body>
</html>
```